lab equipment website

We need a fresh new look for a company website called tarvio. We will be using the current logo and brand colors on their current website tarvio.com. They want to keep their text and on-page SEO, but would like to reformat it to look more modern and fresh. They want to have everything be high performance with a great user experience. Their main call to action is for people to fill in a contact form so they can call them. There is some information that is purposely above the fold on the instrument pages. I will need the home page, about page and a leasing page.

```html
<!DOCTYPE html>
<html lang="en">
<head>
<meta charset="utf-8">
<title>tarvio — Lab Balance Leasing</title>
<link href="https://fonts.googleapis.com/css2?family=Montserrat:wght@400;600;700&family=Roboto:wght@400;500;700&display=swap" rel="stylesheet">
<style>
:root{
  --teal:#13c3a4;
  --teal-dark:#0fa88d;
  --ink:#222427;
  --bar:#3a3b3e;
  --nav:#2f3033;
  --foot:#2b2c2f;
  --mint:#eefaf7;
  --band:#efefef;
  --line:#d9dedd;
  --muted:#6c7173;
  --white:#fff;
}
*{margin:0;padding:0;box-sizing:border-box}
html,body{width:1200px;height:1200px;overflow:hidden;background:#fff}
body{font-family:"Roboto",Arial,sans-serif;color:var(--ink)}
.page{position:absolute;left:324px;top:0;width:690px;height:1500px;transform:scale(.8);transform-origin:0 0;background:var(--mint);overflow:hidden}
.abs{position:absolute}
.topbar{left:0;top:0;width:690px;height:22px;background:var(--bar);color:#cfd2d3;font-size:5.5px}
.dot{display:inline-block;width:10px;height:10px;border-radius:50%;background:#cfd2d3}
.topbar .socials{left:101px;top:6px;display:flex;gap:8px}
.topbar .addr{left:198px;top:8px}
.topbar .mail{left:394px;top:8px}
.topbar .phone{left:510px;top:4px;color:var(--teal);font-size:11.5px;font-weight:500}
.nav{left:0;top:22px;width:690px;height:48px;background:var(--nav)}
.logo{left:102px;top:13px;display:flex;align-items:center;gap:4px;color:#fff;font-family:"Montserrat",sans-serif;font-weight:700;font-size:12px}
.logo i{width:9px;height:9px;background:var(--teal)}
.nav-item{top:0;height:48px;width:46px;color:#b6b9bb;font-size:4.5px;text-align:center;padding-top:31px}
.nav-item::before{content:"";position:absolute;left:19px;top:13px;width:8px;height:8px;border-radius:50%;background:#9a9da0}
.nav-item.active{background:#e3e5e6;color:#9a9da0}
.nav-item.active::before{background:var(--teal);border-radius:1px}
.cart{left:554px;top:0;width:31px;height:48px;background:var(--teal)}
.search-lead{left:270px;top:79px;width:180px;text-align:right;font-size:6px;font-weight:700}
.search-lead b{color:var(--teal)}
.search{left:455px;top:77px;width:98px;height:11px;background:#fff;border:1px solid #e3e5e6;font-size:4.5px;color:#999;padding:3px 8px;font-style:italic}
.search-btn{left:554px;top:77px;width:31px;height:11px;background:var(--ink)}
.hero{left:0;top:70px;width:690px;height:218px;background:linear-gradient(90deg,#e9f7f3,#f6fbfa 60%,#eef4f3)}
.hero-art{left:350px;top:40px;width:340px;height:150px;background:linear-gradient(90deg,#d6dde0,#a9b3b9 45%,#e4e8ea);border-radius:4px}
.hero h1{left:102px;top:47px;font:400 21px "Montserrat",sans-serif;color:#222}
.hero .rule{left:102px;top:78px;width:104px;height:2px;background:var(--teal)}
.hero h2{left:102px;top:85px;font:700 17.5px "Montserrat",sans-serif;color:var(--ink)}
.hero h2 span{color:var(--teal)}
.hero p{left:102px;top:118px;width:240px;font-size:7.6px;line-height:13px;color:#333;text-align:justify}
.btn{height:20px;font-size:6px;font-weight:700;color:#fff;display:flex;align-items:center;justify-content:center}
.learn{left:102px;top:176px;width:71px;background:var(--teal)}
.lease{left:173px;top:176px;width:73px;background:var(--ink)}
.hero .arrow{left:26px;top:118px;width:26px;height:26px;border-radius:50%;background:#e2e8e7}
.dots{display:flex;gap:8px}
.dots i{width:4.5px;height:4.5px;border-radius:50%;border:1px solid var(--teal)}
.dots i.on{background:var(--teal)}
.cats{left:0;top:288px;width:690px;height:165px;background:var(--band)}
.card{top:14px;width:114px;height:114px;border:2px solid #e1e3e4;background:linear-gradient(180deg,#fff,#dfe2e3)}
.card.on{border-color:var(--teal)}
.card .lbl{position:absolute;left:0;right:0;top:80px;height:22px;background:rgba(240,240,240,.8);text-align:center;font:700 8.5px "Montserrat",sans-serif;line-height:22px;color:#333}
.card.on .lbl{color:var(--teal)}
.card .dia{position:absolute;left:50px;top:106px;width:12px;height:12px;background:var(--ink);transform:rotate(45deg)}
.card.on .dia{background:var(--teal)}
.side-head{left:102px;top:474px;width:167px;height:22px;background:var(--teal);color:#fff;font:700 8px "Montserrat",sans-serif;padding:7px 7px}
.side-list{left:102px;top:505px;width:167px;list-style:none}
.side-list li{height:20.1px;border-bottom:1px solid #e6eaea;font-size:6px;padding:6px 6px;color:#333}
.side-list li.on{background:#e1e4e4}
.side-list li.more{color:#999;border:none}
.cta-box{left:108px;top:885px;width:151px;height:28px;background:var(--ink);color:#fff;font:700 6px "Montserrat",sans-serif;letter-spacing:1px;padding:6px 9px;line-height:8px}
.cta-box span{color:var(--teal)}
.cta-text{left:110px;top:922px;width:148px;font-size:5.5px;line-height:12.8px;color:#555}
.cta-text b{color:var(--teal);font-size:10px;font-weight:500}
.cta-text em{font-style:normal;color:var(--teal)}
.form{left:108px;top:990px;width:151px;height:184px;background:var(--nav);padding:13px 9px}
.tabs{display:flex}
.tabs div{flex:1;height:15px;font-size:5px;color:#fff;text-align:center;line-height:15px;background:#4a4c50;font-weight:700}
.tabs div:first-child{background:var(--teal)}
.form h4{color:#fff;font:600 6px "Montserrat",sans-serif;letter-spacing:1.6px;text-align:center;margin:16px 0 9px}
.field{height:15px;border:1px solid #55585c;margin-bottom:6.5px;font-size:4.5px;color:#8a8d90;text-align:center;line-height:13px}
.submit{height:15px;background:var(--teal);color:#fff;font-size:6px;font-weight:700;text-align:center;line-height:15px;margin-top:15px}
.prod-img{left:284px;top:474px;width:95px;height:95px;background:linear-gradient(160deg,#f4f6f7,#c6cfd3);border:1px solid #e1e3e4}
.prod-title{left:390px;top:494px;font:400 20px "Montserrat",sans-serif;letter-spacing:3.5px;color:var(--ink)}
.prod-title span{color:var(--teal)}
.prod-rule{left:390px;top:521px;width:198px;height:1px;background:#d6dada}
.prod-sub{left:392px;top:530px;width:196px;font:600 5.3px "Montserrat",sans-serif;letter-spacing:1px;line-height:8px;color:#444}
.copy{left:282px;width:306px;font-size:5.5px;line-height:13px;color:#555}
.copy.lead{font-size:6.8px;font-weight:700;color:#333}
.bul{list-style:none;padding-left:25px}
.bul li{position:relative;line-height:10px;margin-bottom:4.5px}
.bul li::before{content:"";position:absolute;left:-9px;top:4px;width:2.5px;height:2.5px;border-radius:50%;background:var(--teal)}
.ind{text-indent:18px;text-align:justify;margin-bottom:7px}
.more-btn{left:413px;top:873px;width:40px;height:9px;background:var(--teal);color:#fff;font-size:3.5px;text-align:center;line-height:9px}
.sec-h{left:282px;font:700 6.2px "Montserrat",sans-serif;letter-spacing:1.5px;color:#333}
.sec-h span{color:var(--teal)}
.acc{left:297px;width:283px;list-style:none}
.acc li{height:17.3px;border-bottom:1px solid var(--line);font-size:5.5px;color:#444;padding:5px 4px;display:flex;justify-content:space-between}
.acc li::after{content:"+";color:#999}
.acc li.open{background:#e4e8e8}
.acc li.open::after{content:"−"}
.acc li.sub{padding-left:24px}
.acc li.more{color:#aaa;padding-left:24px}
.acc li.more::after{content:""}
.footer{left:0;top:1350px;width:690px;height:108px;background:var(--foot);color:#fff}
.f-h{top:12px;font:700 6.2px "Montserrat",sans-serif}
.f-rule{top:23px;height:1px;background:#55585c}
.f-rule i{display:block;width:22px;height:2px;background:#e14b4b;margin-top:-.5px}
.f-rule.teal i{background:var(--teal)}
.f-links{left:102px;top:34px;list-style:none;font-size:5.5px;font-weight:700}
.f-links li{height:13px}
.f-contact{left:302px;top:32px;font-size:6px;font-weight:700;line-height:8.5px}
.f-phone{left:302px;top:63px;color:var(--teal);font-size:11px;font-weight:500;letter-spacing:.5px}
.f-web{left:302px;top:78px;font-size:6px;line-height:10px}
.ico{width:5px;height:5px;border-radius:50%;background:var(--teal)}
.nl{left:470px;width:114px;height:11px;background:#c9cbcc;font-size:3.5px;color:#fff;padding:3px 8px}
.nl-btn{left:470px;top:63px;width:114px;height:12px;background:var(--teal);font-size:4.5px;letter-spacing:3px;text-align:center;line-height:12px;font-weight:700}
.f-social{left:470px;top:84px;display:flex;gap:8px}
.f-social .dot{width:12px;height:12px;background:#fff}
.strip{left:0;top:1458px;width:690px;height:20px;background:#55575a;color:#e6e6e6;font-size:5px;text-align:center;line-height:20px}
.copyright{left:0;top:1478px;width:690px;height:22px;background:#1f2022;color:#ddd;font-size:5px;text-align:center;line-height:22px}
</style>
</head>
<body>
<div class="page">

  <header>
    <div class="abs topbar">
      <div class="abs socials"><i class="dot"></i><i class="dot"></i><i class="dot"></i><i class="dot"></i></div>
      <div class="abs addr">48 Harbor Lane&nbsp; Suite 300&nbsp; Fairview, CA 90210</div>
      <div class="abs mail">hello@tarvio.com</div>
      <div class="abs phone">(555) 014-2270</div>
    </div>
    <nav class="abs nav">
      <div class="abs logo"><i></i>tarvio</div>
      <div class="abs nav-item" style="left:195px">HOME</div>
      <div class="abs nav-item" style="left:240px">ABOUT</div>
      <div class="abs nav-item active" style="left:285px">LEASING</div>
      <div class="abs nav-item" style="left:329px">FAQ</div>
      <div class="abs nav-item" style="left:381px;width:44px">CONTACT INFO</div>
      <div class="abs cart">
        <svg width="31" height="48" viewBox="0 0 31 48"><path d="M10 20h2l2 7h6l2-5h-9" fill="none" stroke="#fff" stroke-width="1.2"/><circle cx="15" cy="29" r="1" fill="#fff"/><circle cx="19" cy="29" r="1" fill="#fff"/></svg>
      </div>
    </nav>
    <div class="abs search-lead"><b>HELP YOU TO FIND</b> WHAT YOU ARE&nbsp; LOOKING !</div>
    <div class="abs search">Search keyword here</div>
    <div class="abs search-btn"></div>
  </header>

  <section class="abs hero">
    <div class="abs hero-art" role="img" aria-label="Laboratory instruments: sequencer, chromatography system and microscope"></div>
    <div class="abs arrow"></div>
    <h1 class="abs">Our goal is simple:</h1>
    <div class="abs rule"></div>
    <h2 class="abs"><span>Save labs</span> Time <span>&amp;</span> Money</h2>
    <p class="abs"><b>tarvio</b> is a lab support program that provides scientists with comprehensive maintenance/repair coverage and operating lease solutions at an affordable price.</p>
    <div class="abs btn learn">LEARN MORE</div>
    <div class="abs btn lease">REQUEST LEASE</div>
    <div class="abs dots" style="left:545px;top:187px"><i class="on"></i><i></i><i></i><i></i></div>
  </section>

  <section class="abs cats">
    <div class="abs card on" style="left:102px" role="img" aria-label="Autoclave"><div class="lbl">AUTOCLAVE</div><div class="dia"></div></div>
    <div class="abs card" style="left:225px" role="img" aria-label="Lab balance"><div class="lbl">LAB BALANCE</div><div class="dia"></div></div>
    <div class="abs card" style="left:348px" role="img" aria-label="Centrifuge"><div class="lbl">CENTRIFUGE</div><div class="dia"></div></div>
    <div class="abs card" style="left:471px" role="img" aria-label="Cryostat"><div class="lbl">CRYOSTAT</div><div class="dia"></div></div>
    <div class="abs dots" style="left:324px;top:147px"><i class="on"></i><i></i><i></i><i></i></div>
  </section>

  <aside>
    <div class="abs side-head">FEATURED PRODUCTS</div>
    <ul class="abs side-list">
      <li>AUTOCLAVE</li><li class="on">LAB BALANCE</li><li>CENTRIFUGE</li><li>MICROSCOPE</li><li>CRYOSTAT</li>
      <li>NEXT GENERATION SEQUENCER (NGS)</li><li>FLOW CYTOMETERS</li><li>PCR SYSTEM</li><li>LIQUID HANDLERS</li>
      <li>MICROPLATE READERS</li><li>CLINICAL CHEMISTRY ANALYZERS</li><li>BLOOD BANK ANALYZERS</li><li>PEPTIDE SYNTHESIZERS</li>
      <li>MICROARRAY SCANNERS</li><li>SPECTROPHOTOMETERS</li><li>WESTERN BLOT IMAGING SYSTEM</li><li>LIQUID CHROMATOGRAPHY SYSTEMS</li>
      <li class="more">View More &nbsp;›</li>
    </ul>
    <div class="abs cta-box"><span>CONTACT US TODAY</span> | REQUEST<br>A LEASE ESTIMATE !</div>
    <div class="abs cta-text">Regardless if you're looking to lease a peptide synthesizer or leaseback a lab scale, we can help.<br><span style="display:block;height:4px"></span>Call us at <b>(555) 014-2270</b> or fill out our <em>contact form</em> below to discuss your equipment</div>
    <form class="abs form">
      <div class="tabs"><div>Leave Message</div><div>Request a lease</div></div>
      <h4>START YOUR TRANSACTION !</h4>
      <div class="field">Your Full Name</div>
      <div class="field">Your Email Address</div>
      <div class="field">Phone Number</div>
      <div class="field">Brand of Instrument</div>
      <div class="submit">SUBMIT</div>
    </form>
  </aside>

  <main>
    <div class="abs prod-img" role="img" aria-label="Analytical lab balance with draft shield"></div>
    <div class="abs prod-title"><span>Lab</span> Balance</div>
    <div class="abs prod-rule"></div>
    <div class="abs prod-sub">HOW LABORATORY SCALES WORK &amp; HOW OUR SERVICEVES SAVE YOUR TIME &amp; MONEY</div>

    <p class="abs copy lead" style="top:589px">Here are the advantages of the tarvio lab balance leasing program:</p>
    <ul class="abs copy bul" style="top:612px">
      <li>Near zero upfront costs and the ability to spread out payments over time.</li>
      <li>Payments may be 100% tax deductible*, which yields you additional savings.</li>
      <li>Reduction of equipment downtime through our comprehensive repair coverage.</li>
      <li>tarvio handles the admin work associated with equipment procurement and maintenance.</li>
      <li>With the cash saved through our program, labs are better able to reinvest in their core business and operations (staffing, inventory, marketing/sales, etc.).</li>
    </ul>
    <p class="abs copy lead" style="top:708px">Please consult your tax advisor to determine the full tax implications of leasing equipment.</p>
    <div class="abs copy" style="top:744px">
      <p class="ind">A lab balance is a class of balance designed to measure small mass in the sub-milligram range. The measuring pan of an analytical balance (0.1 mg or better) is inside a transparent enclosure with doors so that dust does not collect and so any air currents in the room do not affect the balance's operation.</p>
      <p class="ind">This enclosure is often called a draft shield. The use of a mechanically vented balance safety enclosure, which has uniquely designed acrylic airfoils, allows a smooth turbulence-free airflow that prevents balance fluctuation and the measure of mass down to 1 µg without fluctuations or loss of product.</p>
      <p class="ind">Also, the sample must be at room temperature to prevent natural convection from forming air currents inside the enclosure from causing an error in reading. Single pan mechanical substitution balance main-</p>
    </div>
    <div class="abs more-btn">VIEW MORE</div>

    <h3 class="abs sec-h" style="top:903px"><span>METHODS &amp; TYPES OF</span> PRESECION WEIGHING</h3>
    <p class="abs copy" style="top:926px">Balances can be found in nearly every laboratory setting throughout the world. Their ability to accurately measure weights and provide detailed data makes them indispensable tools. Below are some of the different types commonly found in laboratories throughout the world.</p>
    <ul class="abs acc" style="top:976px">
      <li>Microbalances &amp; Ultra Micro Balances</li><li>Automated Powder &amp; Liquid Dosing</li><li>Analytical Balances</li>
      <li>Precision Balances</li><li>Moisture Analyzer</li><li>Gold and Carat Balances</li>
    </ul>

    <h3 class="abs sec-h" style="top:1106px"><span>AN ANALYTICAL BALANCE THAT</span> SUITS YOUR NEEDS</h3>
    <ul class="abs acc" style="top:1127px">
      <li>Operating Lease</li><li>Sale Leaseback</li><li class="open">Laboratory Balance Manufacturers &amp; Models on the Market</li>
      <li class="sub">Veltmark</li><li class="sub">Sorrenta</li><li class="sub">Ohlin</li><li class="sub">Kessel &amp; Brandt</li>
      <li class="sub">Shimora</li><li class="sub">Colby-Parr</li><li class="more">View More &nbsp;›</li>
    </ul>
  </main>

  <footer>
    <div class="abs footer">
      <div class="abs f-h" style="left:102px">QUICK LINKS</div>
      <div class="abs f-rule" style="left:102px;width:98px"><i></i></div>
      <ul class="abs f-links"><li>Home</li><li>About Us</li><li>Leasing</li><li>FAQ</li><li>Contact Info</li></ul>

      <div class="abs f-h" style="left:294px">CONTACT INFO</div>
      <div class="abs f-rule teal" style="left:294px;width:98px"><i></i></div>
      <div class="abs ico" style="left:292px;top:34px"></div>
      <div class="abs f-contact">48 Harbor Lane<br>Suite 300<br>Fairview, CA 90210</div>
      <div class="abs ico" style="left:292px;top:68px"></div>
      <div class="abs f-phone">(555) 014-2270</div>
      <div class="abs f-web">info@tarvio.com<br>https://tarvio.com</div>

      <div class="abs f-h" style="left:470px">ALWAYS RECEIVE NEWS LETTER ?</div>
      <div class="abs f-rule teal" style="left:470px;width:114px"><i></i></div>
      <div class="abs nl" style="top:34px">Type your name</div>
      <div class="abs nl" style="top:49px">Type your email</div>
      <div class="abs nl-btn">SUBSCRIBE</div>
      <div class="abs f-social"><i class="dot"></i><i class="dot"></i><i class="dot"></i><i class="dot"></i></div>
    </div>
    <div class="abs strip">We are a team of Bayside University scientists driven by our passion for research. We strive to serve the scientific community. We love what we do, and who we work with. Together we can make positive changes in the world of research.</div>
    <div class="abs copyright">Copyright © 2018 Corvane Studio. All Rights Reserved.</div>
  </footer>

</div>
</body>
</html>
```